Tarnwick Business Card

We need business cards for Tarnwick Consulting. We have a logo that was recently designed. I would obviously like the logo on the card and to stay with similar fonts and colors.

I think the font is Trebuchet MS or something very close to it.
CMYK for the blue is C:100 M:100 Y:0 K:0
And for the green C:40 M:0 Y:40 K:0

Tarnwick Consulting is based in Wellington, New Zealand. Doing consulting and advisory work in Australia, PNG and NZ to government and private organisations.
We provide management guidance and consultancy on petroleum, gas and mineral (predominantly gold) projects. (Geophysical consulting).
We advise on design, contractor selection, tendering, risk assessment through to full project delivery and operational management

We are looking for a professional, corporate looking cards.

Industry/Entity Type

Business

```html
<!DOCTYPE html>
<html lang="en">
<head>
<meta charset="utf-8">
<title>Tarnwick Consulting – Business Card</title>
<link rel="stylesheet" href="https://fonts.googleapis.com/css2?family=Fira+Sans:wght@400;600&display=swap">
<style>
  :root {
    --brand-blue: #232a8f;
    --brand-green: #a9bd12;
    --card-white: #ffffff;
    --stage: #e6e7ea;
    --card-shadow: rgba(20, 22, 40, 0.18);
    --font-body: "Fira Sans", "Trebuchet MS", sans-serif;
  }
  * { box-sizing: border-box; margin: 0; padding: 0; }
  html, body {
    width: 1200px; height: 900px; overflow: hidden;
    background: var(--stage);
    font-family: var(--font-body);
  }
  .canvas {
    width: 1200px; height: 900px;
    display: flex; flex-direction: column;
    align-items: center; justify-content: center; gap: 50px;
  }
  .card {
    position: relative;
    width: 660px; height: 377px;
    background: var(--card-white);
    box-shadow: 0 6px 20px var(--card-shadow);
    overflow: hidden;
    color: var(--brand-blue);
  }

  /* Front */
  .card-front { display: flex; align-items: center; justify-content: center; }
  .wordmark { display: flex; align-items: center; gap: 16px; }
  .wordmark-dot {
    width: 26px; height: 26px; border-radius: 50%;
    background: var(--brand-green);
  }
  .wordmark-name {
    font-size: 38px; font-weight: 400; letter-spacing: 0.5px;
    color: var(--brand-blue);
  }

  /* Back */
  .company-name {
    position: absolute; left: 190px; top: 62px;
    font-size: 34px; font-weight: 400; letter-spacing: 0.5px;
  }
  .person { position: absolute; left: 150px; top: 168px; }
  .person-name { font-size: 20px; font-weight: 400; }
  .person-role { font-size: 12px; font-weight: 600; letter-spacing: 0.8px; margin-top: 4px; }
  .contacts { list-style: none; margin-top: 16px; font-size: 15px; line-height: 21px; }
  .contacts li { display: flex; }
  .contact-key { width: 22px; color: var(--brand-green); font-weight: 600; }
  .address {
    position: absolute; left: 450px; top: 176px;
    padding-left: 16px; border-left: 1.5px solid var(--brand-green);
    font-size: 14px; line-height: 20px; height: 126px;
    font-style: normal;
  }
  .band-blue {
    position: absolute; left: 0; bottom: 0;
    width: 450px; height: 40px; background: var(--brand-blue);
  }
  .band-green {
    position: absolute; right: 0; bottom: 0;
    width: 210px; height: 75px; background: var(--brand-green);
  }
</style>
</head>
<body>
<main class="canvas">
  <section class="card card-front" aria-label="Card front">
    <div class="wordmark">
      <span class="wordmark-dot"></span>
      <span class="wordmark-name">Tarnwick Consulting</span>
    </div>
  </section>

  <section class="card card-back" aria-label="Card back">
    <h1 class="company-name">Tarnwick Consulting</h1>
    <div class="person">
      <p class="person-name">Helena Marsh</p>
      <p class="person-role">DIRECTOR</p>
      <ul class="contacts">
        <li><span class="contact-key">P</span>+64 4381 2257</li>
        <li><span class="contact-key">M</span>+64 2143 5096</li>
        <li><span class="contact-key">E</span>Helena@tarnwickconsulting.co.nz</li>
        <li><span class="contact-key">W</span>www.tarnwickconsulting.co.nz</li>
      </ul>
    </div>
    <address class="address">
      14 Kowhai Terrace<br>
      Ngaio 6035<br>
      Wellington<br>
      New Zealand
    </address>
    <div class="band-blue"></div>
    <div class="band-green"></div>
  </section>
</main>
</body>
</html>
```